Birch Hollow Lodge & Harbour. A site that will sell our lifestyle and embody our vision.

We are after a fun interactive website for our property development.
Check out our ideas for layout and content.
Use stock videos and phots if we havent provide enough.
Ive attached our Logo.
We are easy to reach and work with. Love the crative process.1.Our Vision.. (This clicks through to vision page)
Nestled in the North East corner of Tesko Lake , Sk amidst thousands of acres of natural beauty, a unique community is taking shape. A community that connectS people, nature and play. A place to find those simpler times.

2.Explore..(This clicks through to explore page)
Discover a new life of adventure, on the lake fishing, in the bush on our trail system or maybe the local golf course.

3. Live Here..(This through to Live page)
Birch Hollow has everything you need to start living a full life based in a thriving community.
Slow down and get to know nature and your neighbors

Target Market(s)

35-65 Lake Life

Coding

Coded - Design and coding required

Number of Pages Required

5+ page

Font styles to use
Other font styles liked:
• Anntonio

Colors
00AB8E
00BBA5
67D7C9
C6EFE9
E9F9F6
F0912C
F2A743
F7CA91
FBE8D2
FDF5EE

Requirements
Nice to have
• Interactive

```html
<!DOCTYPE html>
<html lang="en">
<head>
<meta charset="utf-8">
<title>Birch Hollow Lodge &amp; Harbour</title>
<link href="https://fonts.googleapis.com/css2?family=Antonio:wght@400;500;600&family=Playfair+Display:wght@700&family=Poppins:wght@300;400;500;600&display=swap" rel="stylesheet">
<style>
:root{
  --teal:#00BBA5;
  --teal-dark:#00AB8E;
  --mint:#C6EFE9;
  --mint-soft:#E9F9F6;
  --peach:#FBE8D2;
  --peach-mid:#F7CA91;
  --orange:#F0912C;
  --ink:#1d1d1d;
  --text:#3a3a3a;
  --muted:#8a8a8a;
  --line:#d9d9d9;
  --white:#ffffff;
}
*{box-sizing:border-box;margin:0;padding:0}
html,body{width:1200px;height:5276px;overflow:hidden;background:var(--white)}
body{position:relative;font-family:"Poppins",sans-serif;color:var(--text)}
.abs{position:absolute}
.photo{position:absolute;display:block}
.heading{font-family:"Antonio",sans-serif;font-weight:500;color:var(--ink)}
.btn{display:inline-block;background:var(--teal);color:var(--white);font-size:13px;font-weight:500;padding:8px 26px;border-radius:3px;text-decoration:none}

/* hero */
.hero{position:absolute;left:0;top:0;width:1200px;height:800px;background:linear-gradient(180deg,#d9cdca 0%,#e8dedb 30%,#cfcfd3 65%,#b9bcc4 100%)}
.nav{position:absolute;top:26px;left:0;width:1200px;text-align:center}
.nav a{font-size:14px;color:var(--ink);text-decoration:none;margin:0 12px}
.nav-contact{position:absolute;right:20px;top:16px;border:1.5px solid #555;border-radius:4px;padding:7px 16px;font-size:14px;color:var(--ink)}
.brand{position:absolute;left:500px;top:90px;width:200px;text-align:center;color:var(--ink)}
.brand-mark{width:44px;height:44px;border:2px solid var(--ink);margin:0 auto 10px}
.brand-name{font-family:"Poppins",sans-serif;font-weight:600;font-size:18px;letter-spacing:3px;line-height:1.2}
.brand-sub{font-family:"Poppins",sans-serif;font-weight:600;font-size:10px;letter-spacing:2px}
.hero-card{position:absolute;box-shadow:0 6px 20px rgba(0,0,0,.18)}
.hero-card span{position:absolute;left:0;right:0;bottom:28px;text-align:center;color:var(--white);font-size:27px;font-weight:500;letter-spacing:.5px}
.hero-sub{position:absolute;left:0;width:1200px;top:700px;text-align:center;font-size:14px;color:var(--white)}

/* feature rows */
.feature-title{font-size:38px}
.feature-copy{font-size:14px;line-height:1.6;color:var(--text);margin:18px 0 22px;width:330px}
.band-peach{position:absolute;left:0;top:1352px;width:1200px;height:470px;background:var(--peach)}

/* rooms */
.section-title{position:absolute;left:0;width:1200px;text-align:center;font-family:"Antonio",sans-serif;font-weight:500;color:var(--ink);font-size:52px}
.room-panel{position:absolute;left:68px;top:2800px;width:1062px;height:360px;background:var(--white);border-radius:14px;box-shadow:0 10px 40px rgba(0,0,0,.08)}
.room{position:absolute;width:296px;text-align:center}
.room-name{font-size:22px;color:var(--ink);margin-top:24px}
.room-copy{font-size:12px;line-height:1.45;color:var(--muted);margin:6px auto 0;width:240px}
.room-more{font-size:12px;font-weight:600;color:var(--ink);margin-top:6px}
.arrow-btn{position:absolute;width:60px;height:60px;border-radius:50%;background:var(--ink)}
.arrow-btn svg{position:absolute;left:18px;top:18px}

/* why */
.why-sub{position:absolute;left:380px;width:440px;top:3370px;text-align:center;font-size:13px;line-height:1.6;color:var(--muted)}
.why-glow{position:absolute;left:220px;top:3520px;width:420px;height:420px;border-radius:50%;background:radial-gradient(circle,rgba(247,202,145,.35) 0%,rgba(198,239,233,.25) 45%,rgba(255,255,255,0) 70%)}
.why-item{position:absolute;left:100px;width:380px}
.why-num{display:inline-block;background:var(--teal);color:var(--white);font-size:12px;font-weight:600;padding:4px 8px;border-radius:10px 0 10px 0}
.why-head{font-size:15px;font-weight:600;color:var(--ink);margin-top:18px}
.why-copy{font-size:13px;line-height:1.6;color:var(--muted);margin-top:10px;width:330px}

/* testimonials */
.testi-title{position:absolute;left:68px;top:4226px;font-family:"Antonio",sans-serif;font-weight:500;font-size:42px;color:var(--ink)}
.testi-card{position:absolute;left:552px;top:4118px;width:548px;height:330px;background:var(--peach);border-radius:16px;padding:40px 46px}
.testi-text{font-size:15px;line-height:1.55;color:var(--text)}
.testi-name{font-family:"Playfair Display",serif;font-size:17px;color:var(--ink);margin-top:40px}
.testi-dot{position:absolute;top:266px;width:38px;height:38px;border-radius:50%}
.testi-glow{position:absolute;left:0;top:4330px;width:500px;height:200px;background:radial-gradient(ellipse at 20% 60%,rgba(247,202,145,.4),rgba(255,255,255,0) 65%)}

/* cta */
.cta{position:absolute;left:0;top:4512px;width:1200px;height:330px;background:var(--mint);text-align:center}
.cta h2{font-family:"Playfair Display",serif;font-weight:700;font-size:40px;color:var(--ink);margin-top:68px}
.cta p{font-size:14px;color:var(--ink);margin-top:14px}
.cta-btn{display:inline-block;margin-top:34px;background:var(--ink);color:var(--white);font-size:12px;font-weight:500;letter-spacing:1.5px;padding:14px 30px;border-radius:3px}

/* footer */
.foot-brand{position:absolute;left:68px;top:4890px;width:150px;color:var(--ink)}
.foot-brand .brand-mark{width:34px;height:34px;margin:0 0 8px}
.foot-brand .brand-name{font-size:16px;letter-spacing:2px}
.foot-brand .brand-sub{font-size:9px;letter-spacing:1.5px}
.foot-form{position:absolute;left:68px;top:5064px;display:flex}
.foot-input{width:180px;height:40px;border:1px solid var(--line);border-radius:4px 0 0 4px;font-size:11px;color:var(--muted);padding:12px 14px}
.foot-submit{height:40px;background:var(--ink);color:var(--white);font-size:12px;font-weight:500;padding:12px 20px;border-radius:0 4px 4px 0;margin-left:14px}
.foot-col{position:absolute;top:4964px}
.foot-col h4{font-size:14px;font-weight:600;color:var(--ink);margin-bottom:14px}
.foot-col li{list-style:none;font-size:12px;color:var(--text);margin-bottom:10px}
.foot-rule{position:absolute;left:68px;top:5180px;width:1064px;height:1px;background:var(--line)}
.foot-copy{position:absolute;left:0;width:1200px;top:5204px;text-align:center;font-size:12px;color:var(--muted)}
.foot-set{position:absolute;right:68px;top:5204px;font-size:12px;color:var(--ink)}
</style>
</head>
<body>

<header class="hero">
  <div class="photo" role="img" aria-label="Misty lake with a sailing mast at dawn" style="left:0;top:0;width:1200px;height:800px;background:linear-gradient(180deg,rgba(222,208,205,.8),rgba(200,203,210,.6))"></div>
  <nav class="nav">
    <a href="#">Home</a><a href="#">About Us</a><a href="#">Our Vision</a><a href="#">Explore</a><a href="#">Live Here</a>
  </nav>
  <a class="nav-contact">Contact Us</a>
  <div class="brand">
    <div class="brand-mark"></div>
    <div class="brand-name">BIRCH HOLLOW</div>
    <div class="brand-sub">LODGE &amp; HARBOUR</div>
  </div>
  <div class="hero-card" style="left:48px;top:300px;width:332px;height:340px">
    <div class="photo" role="img" aria-label="Mother and child relaxing by a lakeside window" style="inset:0;background:linear-gradient(160deg,#e7dccb,#b6a48b 60%,#6f6250)"></div>
    <span>CONNECT TO PEOPLE</span>
  </div>
  <div class="hero-card" style="left:392px;top:262px;width:402px;height:400px">
    <div class="photo" role="img" aria-label="White lake house among autumn trees" style="inset:0;background:linear-gradient(180deg,#c9c2b9 0%,#b25b2a 40%,#7a4a25 70%,#4d5a3a 100%)"></div>
    <span>CONNECT TO NATURE</span>
  </div>
  <div class="hero-card" style="left:812px;top:300px;width:336px;height:340px">
    <div class="photo" role="img" aria-label="Summer forest trail video" style="inset:0;background:linear-gradient(160deg,#d9e6c2,#7e9a5a 55%,#3e5a32)"></div>
    <svg class="abs" style="left:152px;top:148px" width="30" height="34" viewBox="0 0 30 34"><path d="M2 2 L28 17 L2 32 Z" fill="#ffffff"/></svg>
    <span>CONNECT TO PLAY</span>
  </div>
</header>

<section class="vision">
  <div class="abs" style="left:120px;top:910px">
    <h2 class="heading feature-title">Our Vision</h2>
    <p class="feature-copy">Nestled in the North East corner of Tesko Lake, Sk amidst thousands of acres of natural beauty, a unique community is taking shape. A community that connects people, nature and play. A place to find those simpler times.</p>
    <a class="btn">More</a>
  </div>
  <div class="photo" role="img" aria-label="Sunset over the lake framed by pine branches" style="left:532px;top:900px;width:540px;height:348px;background:linear-gradient(180deg,#b45a55 0%,#e48a5a 40%,#c46a58 55%,#3e3a3d 80%,#1f2327 100%)"></div>
</section>

<section class="band-peach">
  <div class="photo" role="img" aria-label="Lakeside meadow with a cabin under a cloudy sky" style="left:108px;top:100px;width:540px;height:352px;background:linear-gradient(180deg,#d9dde2 0%,#8f9aa6 40%,#6c7f8e 55%,#5f8a4c 75%,#4b6a3c 100%)"></div>
  <div class="abs" style="left:700px;top:118px">
    <h2 class="heading feature-title">Explore</h2>
    <p class="feature-copy">Discover a new life of adventure, on the lake fishing, in the bush on our trail system or maybe the local golf course.</p>
    <a class="btn">More</a>
  </div>
</section>

<section class="live">
  <div class="abs" style="left:120px;top:2018px">
    <h2 class="heading feature-title">Live Here</h2>
    <p class="feature-copy">Birch Hollow has everything you need to start living a full life based in a thriving community.</p>
    <a class="btn">More</a>
  </div>
  <div class="photo" role="img" aria-label="Eagle perched on a branch above the shoreline" style="left:532px;top:2012px;width:540px;height:344px;background:linear-gradient(160deg,#e9e9e6 0%,#bfc3bf 45%,#5d6b55 75%,#33402f 100%)"></div>
</section>

<section class="rooms">
  <h2 class="section-title" style="top:2478px">Relaxing Your Life With Nature</h2>
  <div class="room-panel"></div>
  <div class="room" style="left:128px;top:2600px">
    <div class="photo" role="img" aria-label="Bright room with a green cabinet and dried flowers" style="position:relative;width:296px;height:280px;background:linear-gradient(180deg,#f1efec 0%,#e2ddd6 55%,#3f8f7b 75%,#2f6f60 100%)"></div>
    <div class="room-name">Clichee room</div>
    <p class="room-copy">Rooms provide a great feelings of energy with unique mood inside. Great for your people.</p>
    <div class="room-more">Learn More &nbsp;→</div>
  </div>
  <div class="room" style="left:452px;top:2600px">
    <div class="photo" role="img" aria-label="Walker on a red jetty into the misty lake" style="position:relative;width:296px;height:280px;background:linear-gradient(180deg,#a9b8c9 0%,#c3ced8 50%,#b46a6a 80%,#8e4c4c 100%)"></div>
    <div class="room-name">Outdoor Adventure</div>
    <p class="room-copy">Make a unforgettable experience on your journey with adventure</p>
    <div class="room-more">Learn More &nbsp;→</div>
  </div>
  <div class="room" style="left:772px;top:2600px">
    <div class="photo" role="img" aria-label="Breakfast spread on a lakeview table" style="position:relative;width:296px;height:280px;background:linear-gradient(180deg,#f4f2ef 0%,#e8e2d8 45%,#b8865c 75%,#7a5a3f 100%)"></div>
    <div class="room-name">Breakfast</div>
    <p class="room-copy">Have breakfast experience in your life with best morning scenery</p>
    <div class="room-more">Learn More &nbsp;→</div>
  </div>
  <div class="arrow-btn" style="left:96px;top:2758px"><svg width="24" height="24" viewBox="0 0 24 24"><path d="M19 12H5M11 6l-6 6 6 6" stroke="#fff" stroke-width="2" fill="none"/></svg></div>
  <div class="arrow-btn" style="left:1036px;top:2758px"><svg width="24" height="24" viewBox="0 0 24 24"><path d="M5 12h14M13 6l6 6-6 6" stroke="#fff" stroke-width="2" fill="none"/></svg></div>
</section>

<section class="why">
  <h2 class="section-title" style="top:3266px">Why You Should Choose Us</h2>
  <p class="why-sub">You should choose us because we provide the best accommodation and we have sorted all the hotels here based on their quality.</p>
  <div class="why-glow"></div>
  <div class="why-item" style="top:3470px">
    <span class="why-num">01</span>
    <div class="why-head">We provide the best choice of hotels for you to stay.</div>
    <p class="why-copy">We always prioritise customer comfort and satisfaction. That's why we only accept the best hotels.</p>
  </div>
  <div class="why-item" style="top:3680px">
    <span class="why-num">02</span>
    <div class="why-head">Low price with best quality</div>
    <p class="why-copy">Although the price tends to be cheaper but it will not affect the quality of service, so don't worry.</p>
  </div>
  <div class="why-item" style="top:3890px">
    <span class="why-num">03</span>
    <div class="why-head">Can refund up to 100%</div>
    <p class="why-copy">Don't worry if suddenly you have a problem and want to do a refund, with us you can get a full refund.</p>
  </div>
  <div class="photo" role="img" aria-label="Palm-lined pool at dusk" style="left:672px;top:3468px;width:376px;height:534px;border-radius:18px;background:linear-gradient(180deg,#d8a56c 0%,#c7b9a1 35%,#1f6f8b 65%,#0b4d69 100%)"></div>
  <div class="photo" role="img" aria-label="Lakeside resort lit at evening" style="left:560px;top:3720px;width:312px;height:240px;border-radius:14px;border:5px solid var(--white);box-shadow:0 8px 24px rgba(0,0,0,.18);background:linear-gradient(180deg,#6f8fb4 0%,#c98a5b 50%,#2d4b6a 100%)"></div>
</section>

<section class="testimonials">
  <div class="testi-glow"></div>
  <h2 class="testi-title">Customer Testimonials</h2>
  <div class="testi-card">
    <p class="testi-text">Beyond 5 stars! Stayed last week at this wonderful lodge. Everything exceeds ones wildest dream of a stay. On top they have the most wonderful staff, extremely kind and helpful with every wish. This is indeed a place you do not want to leave, and when you do it is with one hope - to come back.</p>
    <div class="testi-name">-Marisol Dunning-</div>
    <span class="testi-dot" style="left:380px;border:1px solid #c9b9a4;background:var(--peach)"></span>
    <span class="testi-dot" style="left:430px;background:var(--ink)"></span>
    <svg class="abs" style="left:393px;top:279px" width="12" height="12" viewBox="0 0 12 12"><path d="M8 2L4 6l4 4" stroke="#8a7a66" stroke-width="1.5" fill="none"/></svg>
    <svg class="abs" style="left:443px;top:279px" width="12" height="12" viewBox="0 0 12 12"><path d="M4 2l4 4-4 4" stroke="#fff" stroke-width="1.5" fill="none"/></svg>
  </div>
</section>

<section class="cta">
  <h2>What are you waiting for?</h2>
  <p>You can &nbsp;contact us to make your vacation feel awesome.</p>
  <span class="cta-btn">SCHEDULE YOUR VACATION NOW</span>
</section>

<footer>
  <div class="foot-brand">
    <div class="brand-mark"></div>
    <div class="brand-name">BIRCH HOLLOW</div>
    <div class="brand-sub">LODGE &amp; HARBOUR</div>
  </div>
  <div class="foot-form">
    <div class="foot-input">Your Email Here...</div>
    <div class="foot-submit">Subscribe</div>
  </div>
  <div class="foot-col" style="left:844px">
    <h4>Informations</h4>
    <ul><li>Home</li><li>About Us</li><li>Our Vision</li><li>Explore</li><li>Live Here</li></ul>
  </div>
  <div class="foot-col" style="left:1040px">
    <h4>Company</h4>
    <ul><li>Leadership</li><li>News</li><li>Career</li></ul>
  </div>
  <div class="foot-rule"></div>
  <div class="foot-copy">©Birch Hollow. All rights observed</div>
  <div class="foot-set">SET</div>
</footer>

</body>
</html>
```